Professional, elegant brochure for funeral home

We have a funeral home. We would like a 2 sided brochure. On one side will be 3 columns for our cremation options and on the other side would be 2-3 columns of our burial options. Would like to print it and also will be putting it on our website at www.Veltranoserves.com

Use as examples

https://www.bardwellhaven.com/pricing-and-resources/online-cremation-package-options

https://pellingtonmortuary.com/wp-content/uploads/Cremation-with-Ceremony-Plans.pdf

We only need a simple 1page (front and back brochure). Once we have decided on the designer I can provide the final content to be placed on the brochure.

Target Market(s)

We are family owned business so Something soft, inviting, personable and looks professionally done.

Industry/Entity Type

Funeral Home

Requirements
Must have
• Look professional. Easy to read
Nice to have
• Softer Muted comforting colors. No bright colors.

```html
<!DOCTYPE html>
<html lang="en">
<head>
<meta charset="UTF-8">
<title>Burial Options Brochure – Back Side</title>
<link rel="stylesheet" href="https://fonts.googleapis.com/css2?family=Playfair+Display:ital,wght@0,400;0,500;0,600;0,700;1,400;1,500&family=Montserrat:wght@400;500;700&display=swap">
<style>
  :root {
    --page-bg: #e4e4e4;
    --paper: #ffffff;
    --teal-deep: #13645f;
    --teal-band: #1d7d77;
    --teal-soft: #9dcdcb;
    --teal-pill: #4aa9a8;
    --stone: #efedeb;
    --ink: #262626;
    --muted: #8d8d8d;
    --serif: "Playfair Display", Georgia, serif;
    --sans: "Montserrat", Arial, sans-serif;
  }
  * { box-sizing: border-box; margin: 0; padding: 0; }
  html, body { width: 1093px; height: 1200px; overflow: hidden; background: var(--page-bg); }
  .brochure {
    position: absolute; left: 123px; top: 0;
    width: 846px; height: 1200px;
    background: var(--paper); overflow: hidden;
    font-family: var(--sans); color: var(--ink);
    font-variant-numeric: lining-nums;
  }
  .hero-photo {
    position: absolute; left: 0; top: 0; width: 846px; height: 360px;
    background:
      linear-gradient(180deg, rgba(255,255,255,0) 0%, rgba(255,255,255,0) 35%, rgba(255,255,255,.75) 62%, #fff 82%),
      linear-gradient(180deg, #8fb07a 0%, #c9cfc0 22%, #eae6df 40%, #d9d2cc 55%, #e9b8c0 68%, #f2e6e2 80%);
  }
  .hero-title {
    position: absolute; left: 0; width: 100%; top: 148px;
    text-align: center; font-family: var(--serif); font-weight: 400;
    font-size: 92px; letter-spacing: -2px; color: var(--teal-deep); line-height: 1;
  }
  .hero-subtitle {
    position: absolute; left: 0; width: 100%; top: 262px;
    text-align: center; font-family: var(--serif); font-size: 38px;
    color: #555; letter-spacing: -0.5px;
  }
  .wave { position: absolute; left: 0; top: 290px; width: 846px; height: 80px; }

  .plan-col { position: absolute; top: 357px; height: 547px; width: 282px; }
  .plan-col.soft { background: linear-gradient(180deg, #ffffff 0%, #e3f1f0 35%, var(--teal-soft) 72%, var(--teal-soft) 100%); }
  .plan-col.stone { background: var(--stone); }
  .col-left { left: 0; }
  .col-mid { left: 282px; width: 283px; }
  .col-right { left: 565px; width: 281px; }
  .col-divider { position: absolute; top: 392px; height: 500px; border-left: 1px dotted #aaa; }

  .plan-title {
    position: absolute; left: 0; width: 100%;
    text-align: center; font-family: var(--serif); font-weight: 500;
    font-size: 24px; line-height: 31px; color: var(--teal-deep);
  }
  .plan-col .plan-title { top: 40px; }
  .features { position: absolute; list-style: none; font-size: 18px; line-height: 22px; color: #2c3b3b; }
  .plan-col .features { top: 118px; }
  .features li { position: relative; padding-left: 20px; }
  .features li::before {
    content: ""; position: absolute; left: 0; top: 7px;
    width: 9px; height: 9px; border-radius: 50%; background: #1b1b1b;
  }
  .features li.gap { margin-top: 20px; }
  .features li.plain::before { display: none; }
  .features .note { display: block; font-size: 13px; line-height: 16px; }

  .price-pill { position: absolute; height: 69px; background: #fff; text-align: center; }
  .price-pill .label { display: block; margin-top: 7px; font-size: 15px; color: var(--muted); }
  .price-pill .amount { display: block; font-family: var(--serif); font-weight: 700; font-size: 31px; color: var(--teal-deep); line-height: 34px; }
  .pill-left { left: 0; top: 401px; width: 216px; border-radius: 0 35px 35px 0; }
  .pill-right { left: 75px; top: 401px; width: 206px; border-radius: 35px 0 0 35px; }

  .split-price { position: absolute; top: 360px; width: 140px; text-align: center; color: #111; }
  .split-price .kind { display: block; font-weight: 700; font-size: 16px; line-height: 21px; }
  .split-price .label { display: block; font-size: 15px; line-height: 21px; }
  .split-price .amount { display: block; margin-top: 10px; font-family: var(--serif); font-weight: 700; font-size: 31px; line-height: 36px; color: var(--teal-deep); }
  .split-rule { position: absolute; left: 144px; top: 378px; height: 106px; border-left: 2px dotted var(--teal-deep); }

  .graveside-row {
    position: absolute; left: 0; top: 904px; width: 846px; height: 157px;
    background: linear-gradient(180deg, #f1efed 0%, #ffffff 40%, #ffffff 80%, #eeeceb 100%);
  }
  .graveside-row::before { content: ""; position: absolute; left: 55px; right: 40px; top: 0; border-top: 1px dotted #aaa; }
  .graveside-row .plan-title { left: 40px; width: 220px; top: 52px; color: #222; }
  .graveside-row .features { left: 296px; top: 14px; }
  .pill-teal {
    position: absolute; left: 640px; top: 49px; width: 206px; height: 69px;
    background: var(--teal-pill); border-radius: 35px 0 0 35px;
    color: #fff; font-size: 16px; line-height: 21px; padding: 12px 0 0 22px;
  }

  .footer { position: absolute; left: 0; top: 1061px; width: 846px; height: 139px; }
  .footer-bg { position: absolute; left: 0; top: 0; width: 846px; height: 139px; }
  .footer-slogan {
    position: absolute; left: 20px; top: 30px; width: 250px; text-align: center;
    font-family: var(--serif); font-style: italic; font-size: 34px; line-height: 36px; color: var(--teal-deep);
  }
  .footer-contact { position: absolute; left: 340px; top: 30px; width: 460px; text-align: center; }
  .footer-contact .tagline { font-size: 18px; line-height: 22px; color: #333; }
  .footer-contact .phone { font-family: var(--serif); font-weight: 700; font-size: 42px; color: #2b2b2b; line-height: 50px; margin-top: 4px; }
  .footer-contact .web { font-size: 16px; line-height: 20px; letter-spacing: 2.5px; color: #333; }
</style>
</head>
<body>
<main class="brochure">
  <div class="hero-photo" role="img" aria-label="Photo of the funeral home building with white columns behind a bed of pink and white flowers"></div>

  <section class="plan-col soft col-left">
    <h2 class="plan-title">Traditional Funeral<br>Ceremony Plan</h2>
    <ul class="features" style="left:32px;">
      <li>Professional Services</li>
      <li>Transfer of Deceased</li>
      <li>Care &amp; Preparation</li>
      <li>Visitation (2 hours)</li>
      <li class="gap">Funeral Ceremony<span class="note">(at Venue of Choice)</span></li>
      <li>Graveside Ceremony<span class="note">(same day)</span></li>
      <li class="gap">Hearse</li>
      <li>Utility Vehicle</li>
    </ul>
    <div class="price-pill pill-left"><span class="label">Plan Price:</span><span class="amount">$6,245</span></div>
  </section>

  <section class="plan-col stone col-mid">
    <h2 class="plan-title">Visitation Graveside<br>Ceremony Plan</h2>
    <ul class="features" style="left:30px;">
      <li>Professional Services</li>
      <li>Transfer of Deceased</li>
      <li>Care &amp; Preparation</li>
      <li>Visitation (2 hours)</li>
      <li class="gap">Graveside Ceremony</li>
      <li class="gap">Hearse</li>
      <li>Utility Vehicle</li>
    </ul>
    <div class="split-price" style="left:2px;"><span class="kind">Same Day<br>Visitation</span><span class="label">Plan Price:</span><span class="amount">$5,745</span></div>
    <div class="split-rule"></div>
    <div class="split-price" style="left:146px;"><span class="kind">Day Prior<br>Visitation</span><span class="label">Plan Price:</span><span class="amount">$6,145</span></div>
  </section>

  <section class="plan-col soft col-right">
    <h2 class="plan-title">Funeral Ceremony<br>Plan</h2>
    <ul class="features" style="left:30px;">
      <li>Professional Services</li>
      <li>Transfer of Deceased</li>
      <li>Care &amp; Preparation</li>
      <li>Funeral Ceremony<span class="note">(at Venue of Choice)</span></li>
      <li>Graveside Ceremony<span class="note">(same day)</span></li>
      <li class="gap">Hearse</li>
      <li>Utility Vehicle</li>
    </ul>
    <div class="price-pill pill-right"><span class="label">Plan Price:</span><span class="amount">$5,745</span></div>
  </section>

  <div class="col-divider" style="left:282px;"></div>
  <div class="col-divider" style="left:565px;"></div>

  <svg class="wave" viewBox="0 0 846 80" preserveAspectRatio="none" aria-hidden="true">
    <path d="M0 62 C 220 40, 420 60, 560 66 C 700 72, 790 56, 846 38 L846 80 L0 80 Z" fill="#e9e7e6"/>
    <path d="M0 58 C 220 36, 420 52, 560 58 C 700 64, 790 48, 846 32 L846 58 C 790 74, 700 84, 560 78 C 420 72, 220 60, 0 70 Z" fill="var(--teal-band)"/>
  </svg>
  <h1 class="hero-title">Plan for peace!</h1>
  <p class="hero-subtitle">Burial Options</p>

  <section class="graveside-row">
    <h2 class="plan-title">Graveside<br>Ceremony Plan</h2>
    <ul class="features">
      <li>Professional Services</li>
      <li>Transfer of Deceased</li>
      <li>Care &amp; Preparation</li>
      <li>Graveside Ceremony</li>
      <li class="plain">Hearse</li>
      <li>Utility Vehicle</li>
    </ul>
    <div class="pill-teal">Plan Price:<br>$5,645</div>
  </section>

  <footer class="footer">
    <svg class="footer-bg" viewBox="0 0 846 139" preserveAspectRatio="none" aria-hidden="true">
      <defs>
        <linearGradient id="footTeal" x1="0" y1="0" x2="0" y2="1">
          <stop offset="0" stop-color="#cfe5e4"/><stop offset="0.5" stop-color="#a9d3d1"/><stop offset="1" stop-color="#8ec6c4"/>
        </linearGradient>
        <radialGradient id="footGlow" cx="0.55" cy="0.45" r="0.5">
          <stop offset="0" stop-color="#ffffff"/><stop offset="1" stop-color="#ffffff" stop-opacity="0"/>
        </radialGradient>
        <linearGradient id="slogan" x1="0" y1="0" x2="1" y2="1">
          <stop offset="0" stop-color="#8fc6c4"/><stop offset="0.6" stop-color="#e2f0ef"/><stop offset="1" stop-color="#ffffff"/>
        </linearGradient>
      </defs>
      <rect width="846" height="139" fill="url(#footTeal)"/>
      <path d="M270 24 C 420 10, 650 8, 846 10 L846 26 C 650 22, 420 26, 290 36 Z" fill="#9fb9b8" opacity=".7"/>
      <ellipse cx="560" cy="75" rx="300" ry="60" fill="url(#footGlow)"/>
      <path d="M0 0 L230 0 C 280 0, 300 30, 302 70 L304 139 L0 139 Z" fill="url(#slogan)"/>
      <path d="M230 0 C 280 0, 300 30, 302 70 L304 139" fill="none" stroke="#ffffff" stroke-width="3"/>
    </svg>
    <p class="footer-slogan">Proper rest<br>for a loved one!</p>
    <div class="footer-contact">
      <p class="tagline">Call any time, Find us on site. Count on us.</p>
      <p class="phone">(555) 314-2760</p>
      <p class="web">www.veltranofh.com</p>
    </div>
  </footer>
</main>
</body>
</html>
```